Business Card Design Project

I would like a business card created for a new company. This is a holding company that acts as my investment company. It holds real estate and service based companies. The name of the company is Sandorecca which is Italian for Evolution. Defined as development or growth.
We currently have no logo. I really like some of the "different" cards out there. Potentially metallic or grey/black. That looks premium/hi-end and unique. I am not sure if your design would be specific to the card stock I end with our just logo/design/font.
Real Estate

```html
<!DOCTYPE html>
<html lang="it">
<head>
<meta charset="utf-8">
<title>Sandorecca – Business Card</title>
<link rel="stylesheet" href="https://fonts.googleapis.com/css2?family=Archivo:wght@800&family=UnifrakturMaguntia&family=Arimo:wght@400&display=swap">
<style>
  :root {
    --backdrop: #e4e4e6;
    --metal-light: #f4f4f4;
    --metal-mid: #c9c9cb;
    --metal-dark: #8e8e92;
    --band: rgba(255, 255, 255, 0.55);
    --ink: #111111;
    --ink-soft: #2a2a2a;
    --divider: rgba(0, 0, 0, 0.35);
  }
  html, body {
    margin: 0;
    width: 1200px;
    height: 900px;
    overflow: hidden;
    background: var(--backdrop);
  }
  .canvas {
    width: 1200px;
    height: 900px;
    display: flex;
    flex-direction: column;
    align-items: center;
    justify-content: center;
    gap: 60px;
  }
  .card {
    position: relative;
    width: 630px;
    height: 360px;
    border-radius: 6px;
    overflow: hidden;
    box-shadow: 0 10px 30px rgba(0, 0, 0, 0.18);
    background:
      repeating-linear-gradient(90deg,
        rgba(255,255,255,0.10) 0 1px,
        rgba(0,0,0,0.05) 1px 2px,
        rgba(255,255,255,0) 2px 4px),
      linear-gradient(90deg,
        var(--metal-dark) 0%,
        var(--metal-mid) 22%,
        var(--metal-light) 50%,
        var(--metal-mid) 78%,
        var(--metal-dark) 100%);
  }
  .band {
    position: absolute;
    left: 0;
    right: 0;
    top: 50%;
    transform: translateY(-50%);
    background: var(--band);
    display: flex;
    align-items: center;
    justify-content: center;
  }

  /* Back: contact side */
  .card-contact .band { height: 78px; gap: 22px; }
  .identity { text-align: right; }
  .person-name {
    font-family: "UnifrakturMaguntia", serif;
    font-size: 32px;
    line-height: 1;
    color: var(--ink);
    margin: 0;
  }
  .person-role {
    font-family: "Arimo", sans-serif;
    font-size: 11px;
    color: var(--ink-soft);
    margin: 2px 0 0;
  }
  .band-divider {
    width: 1px;
    height: 52px;
    background: var(--divider);
  }
  .contact-list {
    list-style: none;
    margin: 0;
    padding: 0;
    font-family: "Arimo", sans-serif;
    font-size: 11px;
    line-height: 1.45;
    color: var(--ink-soft);
  }

  /* Front: company name */
  .card-brand .band { height: 110px; }
  .company-name {
    font-family: "Archivo", sans-serif;
    font-weight: 800;
    font-size: 62px;
    letter-spacing: -1px;
    color: var(--ink);
    margin: 0;
    text-transform: uppercase;
  }
</style>
</head>
<body>
  <main class="canvas">
    <section class="card card-contact" aria-label="Retro del biglietto">
      <div class="band">
        <div class="identity">
          <p class="person-name">Marco Velli</p>
          <p class="person-role">Manager</p>
        </div>
        <div class="band-divider"></div>
        <ul class="contact-list">
          <li>phone: (312) 480 226 917</li>
          <li>e-mail: marco@sandorecca.com</li>
          <li>www.sandorecca.com</li>
        </ul>
      </div>
    </section>

    <section class="card card-brand" aria-label="Fronte del biglietto">
      <div class="band">
        <h1 class="company-name">Sandorecca</h1>
      </div>
    </section>
  </main>
</body>
</html>
```